Website for Apartment Rental in Prague

I would like to create designs of my website focused on luxury apartment rentals in Prague, Czech Republic. I created initial mock-ups, They are all attached. I need to design homepage and subpage. The mock-ups were created by combining elements from different websites that I liked but I need you to create a design that is unique and original. The attached files a only a guidance for the structure of the website but not for the design. Try to be creative.

Industry/Entity Type

Apartment

```html
<!DOCTYPE html>
<html lang="en">
<head>
<meta charset="utf-8">
<title>Maison Vltava Residences – Property for Sale</title>
<link href="https://fonts.googleapis.com/css2?family=Lato:wght@400;700;900&family=Raleway:wght@500;600;700&display=swap" rel="stylesheet">
<style>
:root{
  --brown:#a08a6b;
  --brown-dark:#8f7a5c;
  --footer:#9c8565;
  --footer-dark:#6f5d45;
  --page:#f4f4f4;
  --white:#ffffff;
  --ink:#2b2b2b;
  --muted:#8a8a8a;
  --line:#e4e4e4;
  --green:#5fae3f;
  --orange:#f6a21a;
  --partner:#9a9a9a;
}
*{box-sizing:border-box;margin:0;padding:0}
html,body{width:1200px;height:2866px;overflow:hidden}
body{background:var(--page);font-family:"Lato",sans-serif;color:var(--ink);position:relative}
.abs{position:absolute}

/* top bar */
.topbar{left:0;top:0;width:1200px;height:57px;background:var(--white);font-size:13px;color:#444}
.topbar span{position:absolute;top:15px}
.brand{position:absolute;left:0;width:1200px;top:7px;text-align:center;font-family:"Raleway",sans-serif;font-weight:700;color:var(--brown-dark);font-size:17px;line-height:20px}
.brand small{display:block;font-size:13px;color:#333;font-weight:700;letter-spacing:.5px}
.mainnav{left:0;top:57px;width:1200px;height:50px;background:var(--white);border-top:1px solid var(--line);border-bottom:1px solid var(--line);display:flex;justify-content:center;gap:42px;align-items:center;font-size:15px;color:#333}
.hero{left:0;top:107px;width:1200px;height:271px;background:linear-gradient(100deg,#4a5461 0%,#d9dde1 22%,#f3f3f1 45%,#e9ebea 65%,#9aa3aa 85%,#3b4048 100%)}

.page-title{left:0;top:424px;width:1200px;text-align:center;font-family:"Raleway",sans-serif;font-weight:700;font-size:42px;letter-spacing:3px;color:var(--brown)}

/* sidebar */
.filters{left:97px;top:520px;width:224px;height:676px;background:var(--white);padding:26px 16px 0}
.filters h4{font-size:12px;font-weight:900;color:#222;margin:14px 0 8px}
.filters h4:first-child{margin-top:0}
.radio{display:flex;align-items:center;font-size:11px;color:#333;height:25px}
.radio i{width:9px;height:9px;border:1.5px solid #333;border-radius:50%;margin-right:9px}
.radio b{margin-left:auto;font-weight:400;color:#666}
.field{height:34px;border:1px solid var(--line);font-size:11px;color:#444;display:flex;align-items:center;padding:0 12px;justify-content:space-between}
.field.caret::after{content:"";border:4px solid transparent;border-top:5px solid #333;margin-top:4px}
.pair{display:flex;gap:10px}.pair .field{flex:1}
.more{font-size:11px;font-weight:700;color:var(--green);text-align:center;margin:14px 0 9px}
.btn-clear{height:33px;background:var(--brown);color:#fff;font-size:11px;font-weight:700;display:flex;align-items:center;justify-content:center}

.guides{left:97px;top:1223px;width:224px;height:359px;background:var(--white);padding:24px 16px}
.guides h4{font-size:15px;font-weight:700;margin-bottom:20px}
.guides p{font-size:12px;line-height:19px;color:#333;padding-bottom:14px;margin-bottom:14px;border-bottom:1px solid var(--line)}
.guides p:last-child{border:0}

/* results */
.toolbar{left:348px;top:520px;width:726px;height:53px;background:var(--white);display:flex;align-items:center;padding:0 14px;font-size:11px;color:#444}
.toolbar .count{margin-left:auto;margin-right:30px}
.sortsel{width:178px;height:28px;background:#eee;margin-left:12px;display:flex;align-items:center;justify-content:space-between;padding:0 12px}
.sortsel::after{content:"";border:4px solid transparent;border-top:5px solid #333;margin-top:4px}
.chips{left:348px;top:592px;height:32px;display:flex;align-items:center;gap:12px;font-size:11px;color:#333}
.chip{height:32px;border:1px solid var(--line);border-radius:16px;background:var(--white);padding:0 16px;display:flex;align-items:center;gap:20px;color:#888}
.chip b{color:#333;font-weight:400}
.clear-all{color:var(--green);margin-left:8px}

.card{left:348px;width:726px;height:142px;background:var(--white);display:flex}
.card .photo{width:233px;height:142px;position:relative}
.photo.day{background:linear-gradient(160deg,#9cc2e8 0%,#dfe8e2 40%,#6f8f4a 75%,#3c5a25 100%)}
.photo.dusk{background:linear-gradient(170deg,#3d4f8c 0%,#8f7fa0 40%,#6a5a4c 70%,#2e2a27 100%)}
.photo.night{background:linear-gradient(170deg,#141a25 0%,#4a3a2c 45%,#c08a45 70%,#2f8fc8 100%)}
.photo.pool{background:linear-gradient(170deg,#b9d6ee 0%,#eef2f2 45%,#7ea06a 70%,#3aa8d8 100%)}
.photo.room{background:linear-gradient(160deg,#e8e2d8 0%,#b58a5c 45%,#5a4a3e 75%,#d9d2c6 100%)}
.tag{position:absolute;left:19px;top:14px;background:var(--orange);color:#fff;font-size:9px;padding:3px 8px}
.heart{position:absolute;right:10px;top:10px;width:27px;height:27px;border-radius:50%;background:rgba(255,255,255,.92);display:flex;align-items:center;justify-content:center}
.card .info{flex:1;padding:18px 25px 0 25px;position:relative}
.cat{font-size:9px;color:var(--green);text-transform:uppercase}
.card h3{font-size:15px;font-weight:700;margin-top:4px}
.addr{font-size:10px;color:var(--muted);margin-top:6px;display:flex;gap:4px;align-items:center}
.stats{display:flex;gap:22px;margin-top:20px}
.stats div{font-size:19px;line-height:19px}
.stats small{display:block;font-size:7px;font-weight:700;color:#444;letter-spacing:.4px;margin-top:3px}
.price{position:absolute;right:25px;top:28px;font-size:15px;font-weight:700;color:var(--brown-dark)}
.details{position:absolute;right:25px;top:92px;width:114px;height:30px;border:1px solid #999;border-radius:15px;font-size:10px;color:#444;display:flex;align-items:center;justify-content:center;gap:6px}

.pager{left:348px;top:2331px;display:flex;gap:8px;font-size:12px;color:#444}
.pager span{width:33px;height:33px;display:flex;align-items:center;justify-content:center}
.pager .on{background:var(--brown);color:#fff;border-radius:3px}

.partners{left:0;top:2444px;width:1200px;height:115px;background:#ececec}
.partner{position:absolute;top:40px;height:34px;background:var(--partner);border-radius:4px;opacity:.7}

.footer{left:0;top:2559px;width:1200px;height:244px;background:var(--footer);color:#fff}
.fcol{position:absolute;top:50px}
.fcol h5{font-family:"Raleway",sans-serif;font-weight:500;font-size:27px;letter-spacing:.5px;margin-bottom:18px}
.fcol a{display:block;font-size:16px;line-height:33px;color:#fff;text-decoration:none;padding-left:3px}
.signup{display:flex;margin-top:6px}
.signup .email{width:191px;height:40px;background:#fff;color:#333;font-size:12px;display:flex;align-items:center;padding-left:14px}
.signup .go{width:113px;height:40px;background:var(--footer-dark);font-size:18px;font-weight:700;display:flex;align-items:center;justify-content:center}
.social{display:flex;gap:10px;margin:12px 0 0 18px}
.social i{width:30px;height:30px;border:1.5px solid #fff;border-radius:50%}
.copy{left:0;top:2803px;width:1200px;height:63px;background:var(--footer);border-top:1px solid rgba(255,255,255,.25);color:#fff;font-size:13px}
.copy p{position:absolute;left:126px;top:16px}
.chat{position:absolute;left:751px;top:11px;width:319px;height:52px;background:#3a3128;display:flex;align-items:center;padding:0 12px;font-size:14px;justify-content:space-between}
.chat b{display:flex;gap:5px}.chat b i{width:19px;height:19px;background:#ddd;border-radius:3px}
</style>
</head>
<body>

<header class="abs topbar">
  <span style="left:120px">OUR HOSPITALITY</span>
  <span style="left:247px">EN ▾</span>
  <span style="left:326px">DISCOVER PRAGUE</span>
  <div class="brand">Maison Vltava<small>RESIDENCES PRAGUE</small></div>
  <span style="left:738px">✉ bookings@vltavaresidences.cz</span>
  <span style="left:957px">✆ +420 700 410 238</span>
</header>
<nav class="abs mainnav">
  <span>APARTMENTS</span><span>LOCATIONS</span><span>SERVICES</span><span>GALLERY</span><span>NEWS</span><span>EXCLUSIVE OFFER &amp; TOURS</span><span>FOR FAMILIES</span><span>CONTACT US</span>
</nav>
<div class="abs hero" role="img" aria-label="Bright modern apartment living room with white sofa and city views"></div>

<h1 class="abs page-title">PROPERTY FOR SALE</h1>

<aside class="abs filters">
  <h4>Property Type</h4>
  <div class="radio"><i></i>ALL<b>(50)</b></div>
  <div class="radio"><i></i>HOUSE/LUXURY<b>(26)</b></div>
  <div class="radio"><i></i>APARTMENT<b>(20)</b></div>
  <div class="radio"><i></i>OFFICE<b>(04)</b></div>
  <h4>City</h4><div class="field caret">All City</div>
  <h4>Keyword</h4><div class="field">Enter keywords...</div>
  <h4>Bedrooms</h4><div class="field caret">All Beds</div>
  <h4>Bathrooms</h4><div class="field caret">All Baths</div>
  <h4>Square Feet (Ft²)</h4><div class="pair"><div class="field caret">No min</div><div class="field caret">No max</div></div>
  <h4>Lot Size</h4><div class="pair"><div class="field caret">No min</div><div class="field caret">No max</div></div>
  <div class="more">MORE FILTER</div>
  <div class="btn-clear">CLEAR FILTER</div>
</aside>

<aside class="abs guides">
  <h4>Get to Know</h4>
  <p>Outer Sunset Real Estate: San Francisco Neighborhood Guide</p>
  <p>Pacific Heights Real Estate: San Francisco CA Neighborhood</p>
  <p>Mission District San Francisco: Authentic Community</p>
  <p>Hayes Valley Real Estate: San Francisco CA Neighborhood</p>
</aside>

<div class="abs toolbar">
  <svg width="14" height="12" viewBox="0 0 14 12"><g fill="#333"><rect x="0" y="0" width="3" height="3"/><rect x="4" y="0" width="10" height="3"/><rect x="0" y="4.5" width="3" height="3"/><rect x="4" y="4.5" width="10" height="3"/><rect x="0" y="9" width="3" height="3"/><rect x="4" y="9" width="10" height="3"/></g></svg>
  <svg width="12" height="12" viewBox="0 0 12 12" style="margin-left:20px"><g fill="#aaa"><rect width="5" height="5"/><rect x="7" width="5" height="5"/><rect y="7" width="5" height="5"/><rect x="7" y="7" width="5" height="5"/></g></svg>
  <span class="count">1-10 of 25 results</span>
  <span>⇅ Sort by</span>
  <div class="sortsel">Default</div>
</div>

<div class="abs chips">
  <span>25 items found</span>
  <span class="chip">Property Type: <b>House</b> ×</span>
  <span class="chip">City: <b>New York</b> ×</span>
  <span class="clear-all">Clear All</span>
</div>

<!-- listing cards -->
<article class="abs card" style="top:644px"><div class="photo day" role="img" aria-label="White villa with garden"><span class="tag">For Sale</span><span class="heart"><svg width="12" height="11" viewBox="0 0 12 11"><path d="M6 10 1.5 5.5A2.6 2.6 0 0 1 6 2a2.6 2.6 0 0 1 4.5 3.5Z" fill="none" stroke="#888"/></svg></span></div><div class="info"><div class="cat">Villa</div><h3>Real House Luxury Villa</h3><div class="addr">⌖ 18 Riverside Lane, 42 - Old Town South, PRG</div><div class="stats"><div>5<sup>+</sup><small>BEDS</small></div><div>3<small>BATHS</small></div><div>1,250<small>SQ.FT</small></div></div><div class="price">$2,285,500</div><div class="details">DETAILS ›</div></div></article>

<article class="abs card" style="top:812px"><div class="photo dusk" role="img" aria-label="Luxury house at dusk"><span class="tag">For Sale</span><span class="heart"><svg width="12" height="11" viewBox="0 0 12 11"><path d="M6 10 1.5 5.5A2.6 2.6 0 0 1 6 2a2.6 2.6 0 0 1 4.5 3.5Z" fill="none" stroke="#888"/></svg></span></div><div class="info"><div class="cat">Luxury House</div><h3>Real House Luxury Villa</h3><div class="addr">⌖ 18 Riverside Lane, 42 - Old Town South, PRG</div><div class="stats"><div>5<sup>+</sup><small>BEDS</small></div><div>3<small>BATHS</small></div><div>1,250<small>SQ.FT</small></div></div><div class="price">$2,285,500</div><div class="details">DETAILS ›</div></div></article>

<article class="abs card" style="top:981px"><div class="photo night" role="img" aria-label="Modern apartment building lit at night with pool"><span class="tag">For Sale</span><span class="heart"><svg width="12" height="11" viewBox="0 0 12 11"><path d="M6 10 1.5 5.5A2.6 2.6 0 0 1 6 2a2.6 2.6 0 0 1 4.5 3.5Z" fill="none" stroke="#888"/></svg></span></div><div class="info"><div class="cat">Apartment</div><h3>Real House Luxury Villa</h3><div class="addr">⌖ 18 Riverside Lane, 42 - Old Town South, PRG</div><div class="stats"><div>5<sup>+</sup><small>BEDS</small></div><div>3<small>BATHS</small></div><div>1,250<small>SQ.FT</small></div></div><div class="price">$2,285,500</div><div class="details">DETAILS ›</div></div></article>

<article class="abs card" style="top:1150px"><div class="photo pool" role="img" aria-label="White modern house with pool"><span class="tag">For Sale</span><span class="heart"><svg width="12" height="11" viewBox="0 0 12 11"><path d="M6 10 1.5 5.5A2.6 2.6 0 0 1 6 2a2.6 2.6 0 0 1 4.5 3.5Z" fill="none" stroke="#888"/></svg></span></div><div class="info"><div class="cat">Luxury House</div><h3>Real House Luxury Villa</h3><div class="addr">⌖ 18 Riverside Lane, 42 - Old Town South, PRG</div><div class="stats"><div>5<sup>+</sup><small>BEDS</small></div><div>3<small>BATHS</small></div><div>1,250<small>SQ.FT</small></div></div><div class="price">$2,285,500</div><div class="details">DETAILS ›</div></div></article>

<article class="abs card" style="top:1319px"><div class="photo room" role="img" aria-label="Open dining room interior"><span class="tag">For Sale</span><span class="heart"><svg width="12" height="11" viewBox="0 0 12 11"><path d="M6 10 1.5 5.5A2.6 2.6 0 0 1 6 2a2.6 2.6 0 0 1 4.5 3.5Z" fill="none" stroke="#888"/></svg></span></div><div class="info"><div class="cat">Apartment</div><h3>Real House Luxury Villa</h3><div class="addr">⌖ 18 Riverside Lane, 42 - Old Town South, PRG</div><div class="stats"><div>5<sup>+</sup><small>BEDS</small></div><div>3<small>BATHS</small></div><div>1,250<small>SQ.FT</small></div></div><div class="price">$2,285,500</div><div class="details">DETAILS ›</div></div></article>

<article class="abs card" style="top:1487px"><div class="photo dusk" role="img" aria-label="Villa at dusk"><span class="tag">For Sale</span><span class="heart"><svg width="12" height="11" viewBox="0 0 12 11"><path d="M6 10 1.5 5.5A2.6 2.6 0 0 1 6 2a2.6 2.6 0 0 1 4.5 3.5Z" fill="none" stroke="#888"/></svg></span></div><div class="info"><div class="cat">Villa</div><h3>Real House Luxury Villa</h3><div class="addr">⌖ 18 Riverside Lane, 42 - Old Town South, PRG</div><div class="stats"><div>5<sup>+</sup><small>BEDS</small></div><div>3<small>BATHS</small></div><div>1,250<small>SQ.FT</small></div></div><div class="price">$2,285,500</div><div class="details">DETAILS ›</div></div></article>

<article class="abs card" style="top:1656px"><div class="photo day" role="img" aria-label="White luxury house with garden"><span class="heart"><svg width="12" height="11" viewBox="0 0 12 11"><path d="M6 10 1.5 5.5A2.6 2.6 0 0 1 6 2a2.6 2.6 0 0 1 4.5 3.5Z" fill="none" stroke="#888"/></svg></span></div><div class="info"><div class="cat">Luxury House</div><h3>Real House Luxury Villa</h3><div class="addr">⌖ 18 Riverside Lane, 42 - Old Town South, PRG</div><div class="stats"><div>5<sup>+</sup><small>BEDS</small></div><div>3<small>BATHS</small></div><div>1,250<small>SQ.FT</small></div></div><div class="price">$2,285,500</div><div class="details">DETAILS ›</div></div></article>

<article class="abs card" style="top:1825px"><div class="photo room" role="img" aria-label="Villa dining room interior"><span class="tag">For Sale</span><span class="heart"><svg width="12" height="11" viewBox="0 0 12 11"><path d="M6 10 1.5 5.5A2.6 2.6 0 0 1 6 2a2.6 2.6 0 0 1 4.5 3.5Z" fill="none" stroke="#888"/></svg></span></div><div class="info"><div class="cat">Villa</div><h3>Real House Luxury Villa</h3><div class="addr">⌖ 18 Riverside Lane, 42 - Old Town South, PRG</div><div class="stats"><div>5<sup>+</sup><small>BEDS</small></div><div>3<small>BATHS</small></div><div>1,250<small>SQ.FT</small></div></div><div class="price">$2,285,500</div><div class="details">DETAILS ›</div></div></article>

<article class="abs card" style="top:1993px"><div class="photo pool" role="img" aria-label="Modern apartment house with pool"><span class="tag">For Sale</span><span class="heart"><svg width="12" height="11" viewBox="0 0 12 11"><path d="M6 10 1.5 5.5A2.6 2.6 0 0 1 6 2a2.6 2.6 0 0 1 4.5 3.5Z" fill="none" stroke="#888"/></svg></span></div><div class="info"><div class="cat">Apartment</div><h3>Real House Luxury Villa</h3><div class="addr">⌖ 18 Riverside Lane, 42 - Old Town South, PRG</div><div class="stats"><div>5<sup>+</sup><small>BEDS</small></div><div>3<small>BATHS</small></div><div>1,250<small>SQ.FT</small></div></div><div class="price">$2,285,500</div><div class="details">DETAILS ›</div></div></article>

<article class="abs card" style="top:2161px"><div class="photo night" role="img" aria-label="Villa lit at night with pool"><span class="tag">For Sale</span><span class="heart"><svg width="12" height="11" viewBox="0 0 12 11"><path d="M6 10 1.5 5.5A2.6 2.6 0 0 1 6 2a2.6 2.6 0 0 1 4.5 3.5Z" fill="none" stroke="#888"/></svg></span></div><div class="info"><div class="cat">Villa</div><h3>Real House Luxury Villa</h3><div class="addr">⌖ 18 Riverside Lane, 42 - Old Town South, PRG</div><div class="stats"><div>5<sup>+</sup><small>BEDS</small></div><div>3<small>BATHS</small></div><div>1,250<small>SQ.FT</small></div></div><div class="price">$2,285,500</div><div class="details">DETAILS ›</div></div></article>

<nav class="abs pager"><span>‹</span><span class="on">1</span><span>2</span><span>3</span><span>›</span></nav>

<section class="abs partners" aria-label="Partners">
  <div class="partner" style="left:146px;width:120px"></div>
  <div class="partner" style="left:340px;width:118px"></div>
  <div class="partner" style="left:538px;width:130px"></div>
  <div class="partner" style="left:728px;width:126px"></div>
  <div class="partner" style="left:935px;width:106px"></div>
</section>

<footer class="abs footer">
  <div class="fcol" style="left:124px"><h5>OUR INFO</h5><a>HOMEPAGE</a><a>ABOUT US</a><a>HIRING</a></div>
  <div class="fcol" style="left:304px"><h5>BOOKING</h5><a>BOOKING PAGE</a><a>BLOG</a></div>
  <div class="fcol" style="left:478px"><h5>ADDITIONAL LINKS</h5><a>GIFT CARD</a><a>HELP</a><a>WE'RE GREEN</a></div>
  <div class="fcol" style="left:762px"><h5>STAY CONNECTED</h5>
    <div class="signup"><div class="email">EMAIL</div><div class="go">SIGN UP</div></div>
    <div class="social"><i></i><i></i><i></i><i></i></div>
  </div>
</footer>
<div class="abs copy">
  <p>Copyright Interiors Designed By Maison Vltava @2017</p>
  <div class="chat">Live Chat<b><i></i><i></i></b></div>
</div>

</body>
</html>
```